Business Card Design Project

We need a logo design for a new company based in Southern California called "Brocklin Security Services, Inc." We install security and camera systems for homeowners and business, to protect their assets.
Updates

Project Deadline Extended
Reason: LOGO Design completes in eight days. Would like that design decided before we finish the business cards. Thanks...

Target Market(s)

Homeowners and business owners looking for additional protection of their assets.

Industry/Entity Type

Security

Font styles to use
Serif

Requirements
Must have
• Company Name
Office# 555-204-6137
Service# 555-204-6138
email: BrocklinSecurity@quorvex.net
address: 48210 Maple Row Harlow Springs, CA 90000
Nice to have
• Serving Southern California

```html
<!DOCTYPE html>
<html lang="en">
<head>
<meta charset="utf-8">
<title>Brocklin Security Services, Inc. — Business Card</title>
<link rel="stylesheet" href="https://fonts.googleapis.com/css2?family=Open+Sans:wght@400;600;700&family=Playfair+Display+SC:wght@700&display=swap">
<style>
  :root {
    --backdrop: #1c1c1e;
    --card: #f7f7f5;
    --brand-red: #e01f2d;
    --ink: #1d1d1f;
    --muted: #55575a;
  }
  html, body {
    margin: 0;
    width: 1200px;
    height: 757px;
    overflow: hidden;
    background: var(--backdrop);
  }
  .card {
    position: absolute;
    left: 150px;
    top: 121px;
    width: 900px;
    height: 514px;
    background: var(--card);
    overflow: hidden;
    font-family: "Open Sans", Arial, sans-serif;
    color: var(--muted);
  }
  .card__shapes {
    position: absolute;
    inset: 0;
  }
  .holder {
    position: absolute;
    left: 92px;
    top: 100px;
  }
  .holder__name {
    margin: 0;
    font-size: 26px;
    font-weight: 700;
    color: var(--ink);
    line-height: 1.1;
  }
  .holder__role {
    margin: 0;
    font-size: 17px;
    color: var(--brand-red);
    line-height: 1.2;
  }
  .company-name {
    position: absolute;
    left: 92px;
    top: 168px;
    margin: 0;
    font-family: "Playfair Display SC", Georgia, serif;
    font-weight: 700;
    font-size: 36px;
    color: var(--brand-red);
    letter-spacing: 0.5px;
    white-space: nowrap;
  }
  .brand-mark {
    position: absolute;
    right: 70px;
    top: 70px;
    display: flex;
    align-items: center;
    gap: 12px;
  }
  .brand-mark__dot {
    width: 34px;
    height: 34px;
    border-radius: 50%;
    background: var(--brand-red);
  }
  .brand-mark__name {
    font-family: "Open Sans", Arial, sans-serif;
    font-weight: 700;
    font-size: 30px;
    color: var(--ink);
  }
  .contact {
    position: absolute;
    margin: 0;
    padding: 0;
    list-style: none;
    font-size: 18px;
  }
  .contact li {
    display: flex;
    align-items: center;
    gap: 16px;
    height: 30px;
    white-space: nowrap;
  }
  .contact svg {
    width: 18px;
    height: 18px;
    fill: var(--brand-red);
    flex: none;
  }
  .contact--phones {
    left: 100px;
    top: 270px;
  }
  .contact--phones li + li { margin-top: 30px; }
  .contact--details {
    left: 360px;
    top: 258px;
  }
  .contact--details li + li { margin-top: 22px; }
</style>
</head>
<body>
  <article class="card">
    <svg class="card__shapes" viewBox="0 0 900 514" width="900" height="514" aria-hidden="true">
      <path d="M0 0 H190 C130 8 60 14 0 30 Z" fill="var(--brand-red)"/>
      <path d="M560 514 C575 440 650 420 740 420 C830 420 880 390 900 330 V514 Z" fill="var(--brand-red)"/>
    </svg>

    <div class="holder">
      <p class="holder__name">Dana Wexler</p>
      <p class="holder__role">Manager</p>
    </div>

    <h1 class="company-name">Brocklin Security Services, Inc</h1>

    <div class="brand-mark">
      <span class="brand-mark__dot"></span>
      <span class="brand-mark__name">Brocklin</span>
    </div>

    <ul class="contact contact--phones">
      <li>
        <svg viewBox="0 0 24 24"><path d="M6.6 10.8a15.1 15.1 0 0 0 6.6 6.6l2.2-2.2a1 1 0 0 1 1-.25 11.4 11.4 0 0 0 3.6.57 1 1 0 0 1 1 1V20a1 1 0 0 1-1 1A17 17 0 0 1 3 4a1 1 0 0 1 1-1h3.5a1 1 0 0 1 1 1c0 1.25.2 2.45.57 3.6a1 1 0 0 1-.25 1z"/></svg>
        <span>555-204-6137</span>
      </li>
      <li>
        <svg viewBox="0 0 24 24"><path d="M6.6 10.8a15.1 15.1 0 0 0 6.6 6.6l2.2-2.2a1 1 0 0 1 1-.25 11.4 11.4 0 0 0 3.6.57 1 1 0 0 1 1 1V20a1 1 0 0 1-1 1A17 17 0 0 1 3 4a1 1 0 0 1 1-1h3.5a1 1 0 0 1 1 1c0 1.25.2 2.45.57 3.6a1 1 0 0 1-.25 1z"/></svg>
        <span>555-204-6138</span>
      </li>
    </ul>

    <ul class="contact contact--details">
      <li>
        <svg viewBox="0 0 24 24"><rect x="2" y="5" width="20" height="14" rx="1.5"/><path d="M3 6.5l9 6.5 9-6.5" fill="none" stroke="var(--card)" stroke-width="1.8"/></svg>
        <span>BrocklinSecurity@quorvex.net</span>
      </li>
      <li>
        <svg viewBox="0 0 24 24"><path d="M12 2a7 7 0 0 0-7 7c0 5 7 13 7 13s7-8 7-13a7 7 0 0 0-7-7zm0 9.5A2.5 2.5 0 1 1 12 6.5a2.5 2.5 0 0 1 0 5z"/></svg>
        <span>48210 Maple Row Harlow Springs, CA 90000</span>
      </li>
    </ul>
  </article>
</body>
</html>
```